UK Based Internet hosting Company wants a vibrant eCommerce site designed.

We have only just had our logo and brand designed by Pixel Harbor which went so well that we would like to open up our website design project on here too.

The company is called 'Our Server Lantern' and we provide a range of website hosting, dedicated server, domain name and email solutions that people will be able to purchase online in neatly packaged options from the outset.

Our logo and brand is bright turquoise, black & white (samples of branding will be attached with this project) but we would like the website to be very vibrant with good use of white space rather than a black website.

We want to appeal to end users so web designers, developers and people who would like to host their website. But we also want to appeal to resellers that would like to resell our hosting packages too.

We want a big push on social media and blogging on the site as we would like our brand to be 100% up with Chatterly, Quipster, workRing, Vidoplex and Orbitly+. It would be great to have this integrated into the site with share buttons and rating buttons etc.

We would like to see a homepage initially with a view to providing several page layers down to help our in-house developers hook in our back-end into this front end effectively.

Great customer experience and an easy to navigate journey to the checkout when purchasing the hosting packages is paramount !!

We like how the following sites are set-out and presented:

www.plumwebnode.uk
http://www.tagvault.co.uk
https://www.zq7.net/web-hosting/

Target Market(s)

We have 3 target markets.

Target market 1 - end users, consumers such as Web Designers, Developers and small businesses.

Target Market 2 - Resellers, small businesses that would like to resell our services.

Target Market 3 - Medium to large businesses that would like more of a bespoke solution.

Industry/Entity Type

Internet

Requirements
Must have
• Colourful, bright, bold, easy to navigate and to purchase packages.
• Plenty of call to actions, social media, ratings.
• Video case studies and testimonials would be nice.

```html
<!DOCTYPE html>
<html lang="en">
<head>
<meta charset="utf-8">
<title>Our Server Lantern – Web Hosting</title>
<link rel="stylesheet" href="https://fonts.googleapis.com/css2?family=Raleway:wght@300;400;600;700&family=Open+Sans:wght@400;600;700&display=swap">
<style>
:root{
  --teal:#1fb3b6;
  --teal-dark:#17989b;
  --ink:#1b1b1b;
  --ink-2:#242424;
  --text:#444;
  --muted:#888;
  --line:#dcdcdc;
  --white:#fff;
  --paper:#f3f3f3;
}
*{box-sizing:border-box;margin:0;padding:0}
html,body{width:1200px;height:4651px;overflow:hidden}
body{font-family:"Open Sans",Arial,sans-serif;color:var(--text);font-size:14px;background:var(--white)}
.wrap{width:1000px;margin:0 auto;position:relative}
h1,h2,h3,.display{font-family:"Raleway",Arial,sans-serif}

/* header */
.site-header{height:110px;background:var(--ink);position:relative}
.site-header .wrap{display:flex;align-items:center;height:110px}
.brand{display:flex;align-items:center;gap:12px;color:var(--white)}
.brand-mark{width:60px;height:60px;border-radius:50%;background:var(--teal)}
.brand-name{font-family:"Raleway",sans-serif;font-size:22px;line-height:1.05;font-weight:600}
.brand-name span{display:block;font-weight:300;letter-spacing:2px}
.main-nav{display:flex;margin-left:auto;margin-right:36px;gap:0}
.main-nav a{color:var(--white);text-decoration:none;font-size:14px;padding:10px 13px;position:relative}
.main-nav a.active{background:var(--teal)}
.dropdown{position:absolute;top:48px;left:0;width:150px;background:var(--teal);padding:6px 0;z-index:3}
.dropdown span{display:block;font-size:12px;padding:8px 12px;color:var(--white)}
.btn-login{position:absolute;right:0;top:12px;background:var(--teal);color:var(--white);font-size:13px;padding:6px 18px;border-radius:2px}

/* hero */
.hero{height:610px;background:linear-gradient(180deg,#f5f5f5 0%,#e8e8e8 55%,#cfcfcf 100%);text-align:center;position:relative;overflow:hidden}
.hero h1{font-size:42px;font-weight:400;color:var(--ink);padding-top:38px}
.search{display:flex;width:640px;margin:24px auto 0;height:56px}
.search div{flex:1;background:var(--white);text-align:left;padding:18px 20px;font-size:13px;color:#aaa}
.search span{width:110px;background:var(--teal);color:var(--white);font-weight:600;line-height:56px;font-size:17px}
.top-domains{margin-top:20px;font-size:18px;color:var(--ink)}
.top-domains b{color:var(--teal);font-weight:600;margin-right:30px}
.top-domains i{font-style:normal;margin:0 14px}
.servers{width:520px;height:300px;margin:34px auto 0;background:linear-gradient(180deg,#d6d6d6,#9fa7a7 60%,#5f6b6b);border-radius:6px}

.strip{height:92px;background:var(--ink-2);color:#ddd;text-align:center;font-size:16px;line-height:26px;padding-top:20px}

/* section heads */
.sec-head{display:flex;gap:26px;align-items:flex-start}
.sec-title{width:250px;flex:none;border-right:1px solid #ccc;padding-right:20px}
.sec-title small{display:block;font-family:"Raleway",sans-serif;font-size:30px;font-weight:400;color:var(--ink);letter-spacing:1px}
.sec-title strong{display:block;font-family:"Raleway",sans-serif;font-size:64px;font-weight:700;color:var(--teal);line-height:1;letter-spacing:2px}
.sec-head p{font-size:13px;line-height:20px;padding-top:4px}
.dark .sec-title small{color:var(--white)}
.dark .sec-title{border-color:#666}
.dark .sec-head p{color:#ddd}

/* plans */
.plans{height:728px;padding-top:42px}
.plan-row{display:flex;gap:20px;margin-top:42px;align-items:flex-start}
.plan{width:235px;border:1px solid var(--line);text-align:center;padding-bottom:26px;background:var(--white)}
.plan h3{font-size:36px;font-weight:700;color:var(--ink);padding:22px 0 10px}
.plan .price{font-family:"Raleway",sans-serif;font-size:40px;color:var(--ink);border-top:1px solid var(--line);border-bottom:1px solid var(--line);padding:10px 0}
.plan .price sub{font-size:14px;vertical-align:baseline}
.plan ul{list-style:none;font-size:14px;line-height:42px;padding-top:4px}
.plan .btn{display:inline-block;background:var(--teal);color:var(--white);padding:7px 30px;font-size:15px;margin-top:10px;border:2px solid var(--teal)}
.plan.featured{background:var(--teal);border-color:var(--teal);color:var(--white);padding-bottom:40px;margin-top:-20px}
.plan.featured h3,.plan.featured .price{color:var(--white)}
.plan.featured .price{border-color:rgba(255,255,255,.5);background:var(--teal-dark)}
.plan.featured ul{font-weight:600}
.plan.featured .btn{border-color:var(--white);background:transparent}

/* features */
.features{height:698px;background:linear-gradient(135deg,#141414,#2a2c2c 50%,#121212);padding-top:40px;color:var(--white)}
.feature-grid{display:grid;grid-template-columns:1fr 1fr;column-gap:40px;row-gap:44px;margin-top:90px}
.feature{display:flex;gap:24px}
.feature svg{flex:none;width:60px;height:60px}
.feature h3{font-size:21px;font-weight:700;margin-bottom:8px}
.feature p{font-size:13px;line-height:20px;color:#e3e3e3}

/* blogs */
.blogs{height:747px;padding-top:40px}
.blog-grid{display:grid;grid-template-columns:1fr 1fr;column-gap:50px;row-gap:28px;margin-top:40px}
.post{display:flex;gap:16px;background:var(--paper);padding:14px;height:156px}
.post .thumb{width:128px;height:128px;flex:none;background:linear-gradient(160deg,#cfd3d6,#8a9096)}
.post h3{font-family:"Open Sans",sans-serif;font-size:14px;font-weight:700;color:var(--ink)}
.post time{display:block;font-size:12px;color:var(--muted);margin:4px 0 6px}
.post p{font-size:13px;line-height:18px;color:#666}
.post a{display:block;color:var(--teal);font-size:13px;margin-top:8px;text-decoration:underline}

/* testimonials */
.testimonials{height:509px;background:linear-gradient(160deg,#181818,#2b2d2d 60%,#151515);padding-top:38px;color:var(--white)}
.quotes{position:relative;height:300px;margin-top:40px}
.quote{position:absolute;display:flex;align-items:center;gap:20px}
.quote .avatar{width:140px;height:140px;border-radius:50%;border:6px solid var(--teal);background:linear-gradient(160deg,#777,#3a3a3a)}
.quote h4{font-size:15px;font-weight:700}
.quote .role{font-size:13px;margin:2px 0 8px}
.quote .role span{color:var(--teal)}
.quote p{font-size:13px;line-height:18px;width:260px}
.quote.left{left:10px;top:0;text-align:right}
.quote.right{left:300px;top:100px}

/* stats */
.stats{height:449px;position:relative;background:linear-gradient(180deg,#c9d6df 0%,#a9a197 45%,#b7a894 100%)}
.stat-row{position:absolute;left:0;right:0;top:110px;display:flex;justify-content:center;gap:170px}
.stat{width:210px;height:210px;border-radius:50%;border:5px solid var(--teal);background:rgba(20,40,45,.8);color:var(--white);text-align:center;padding-top:44px}
.stat b{font-family:"Raleway",sans-serif;font-size:40px;font-weight:600;display:block}
.stat span{font-size:13px;display:block;margin:6px 0 16px}
.stat em{font-style:normal;font-size:12px;background:var(--white);color:var(--ink);padding:4px 10px;border-radius:2px}

/* clients */
.clients{height:344px;padding-top:46px}
.client-row{display:flex;justify-content:space-between;align-items:center;margin-top:70px;padding:0 20px}
.client{font-family:"Raleway",sans-serif;font-size:26px;font-weight:700;color:var(--ink);display:flex;align-items:center;gap:10px}
.client i{width:22px;height:22px;background:var(--teal);border-radius:50%;display:block}

/* footer */
.site-footer{height:326px;background:var(--ink);color:#ddd;position:relative;overflow:hidden}
.footer-cols{display:flex;gap:0;padding-top:36px}
.footer-col{width:220px}
.footer-col h4{font-family:"Raleway",sans-serif;font-size:22px;color:var(--white);font-weight:400;margin-bottom:16px;letter-spacing:1px}
.footer-col ul{list-style:none;font-size:13px;line-height:20px}
.footer-col li::before{content:"»";margin-right:10px;color:var(--teal)}
.contact{width:280px}
.contact div{font-size:13px;line-height:18px;margin-bottom:14px;padding-left:34px;position:relative}
.contact div svg{position:absolute;left:0;top:0}
.contact .phone{font-size:24px;color:var(--white);line-height:28px}
.follow{position:absolute;right:0;top:0;width:370px;height:326px;background:var(--teal);padding:36px 0 0 40px;color:var(--white)}
.follow h4{font-family:"Raleway",sans-serif;font-size:24px;font-weight:400;letter-spacing:1px;margin-bottom:12px}
.socials{display:flex;gap:10px;margin-bottom:24px}
.socials i{width:26px;height:26px;background:var(--white);border-radius:50%;display:block}
.newsletter{width:240px;height:34px;background:var(--white);color:#aaa;font-size:12px;padding:9px 12px;margin:14px 0 10px}
.submit{display:inline-block;background:var(--white);color:var(--ink);font-size:12px;font-weight:700;padding:5px 14px;border-radius:2px}
.bottom-bar{height:38px;background:#efefef;font-size:12px;color:#333}
.bottom-bar .wrap{display:flex;justify-content:space-between;line-height:38px}
.bottom-bar nav span{margin-left:20px}
</style>
</head>
<body>

<header class="site-header">
  <div class="wrap">
    <div class="brand">
      <div class="brand-mark"></div>
      <div class="brand-name">Our Server<span>LANTERN</span></div>
    </div>
    <nav class="main-nav">
      <a>Home</a><a>Layouts</a><a>Domains</a>
      <a class="active">Hosting<div class="dropdown"><span>Shared Hosting</span><span>Premium Hosting</span></div></a>
      <a>Elements</a><a>Pages</a><a>Portfolio</a><a>Contact</a>
    </nav>
    <span class="btn-login">Login</span>
  </div>
</header>

<section class="hero">
  <h1>Empowering you to take control of your internet bubble</h1>
  <div class="search"><div>Enter Your Domain Name Here</div><span>Search</span></div>
  <p class="top-domains"><b>Top Domains</b><i>.com $11.99</i><i>.org $11.99</i><i>.net $10.99</i></p>
  <div class="servers" role="img" aria-label="Row of server towers with turquoise trim"></div>
</section>

<div class="strip">
  We have registered over 2 million domain names and host over 1.9 million websites for individuals and organizations<br>
  Our fast and flexible website creator is the easy way to build &amp; manage a site for your business
</div>

<section class="plans">
  <div class="wrap">
    <div class="sec-head">
      <h2 class="sec-title"><small>MOST POPULAR</small><strong>PLANS</strong></h2>
      <p>Lorem Ipsum has been the industry's standard dummy text ever since the 1500s, when an unknown printer took a galley of type and scrambled it to make a type specimen book. It has survived not only five centuries, but also the leap into electronic typesetting.</p>
    </div>
    <div class="plan-row">
      <div class="plan featured"><h3>Basic</h3><div class="price">$9.99 <sub>/mo</sub></div>
        <ul><li>1 GB Bandwidth</li><li>256 MB Memory</li><li>24/7 Full Support</li><li>Free Domain Name</li><li>Money back Guarantee</li></ul><span class="btn">Sign Up</span></div>
      <div class="plan"><h3>Standard</h3><div class="price">$28.9 <sub>/mo</sub></div>
        <ul><li>1 GB Bandwidth</li><li>256 MB Memory</li><li>24/7 Full Support</li><li>Free Domain Name</li><li>Money back Guarantee</li></ul><span class="btn">Sign Up</span></div>
      <div class="plan"><h3>Premium</h3><div class="price">$38.9 <sub>/mo</sub></div>
        <ul><li>1 GB Bandwidth</li><li>256 MB Memory</li><li>24/7 Full Support</li><li>Free Domain Name</li><li>Money back Guarantee</li></ul><span class="btn">Sign Up</span></div>
      <div class="plan"><h3>Unlimited</h3><div class="price">$68.9 <sub>/mo</sub></div>
        <ul><li>1 GB Bandwidth</li><li>256 MB Memory</li><li>24/7 Full Support</li><li>Free Domain Name</li><li>Money back Guarantee</li></ul><span class="btn">Sign Up</span></div>
    </div>
  </div>
</section>

<section class="features dark">
  <div class="wrap">
    <div class="sec-head">
      <h2 class="sec-title"><small>OUR EXCELLENT</small><strong>FEATURES</strong></h2>
      <p>Lorem Ipsum has been the industry's standard dummy text ever since the 1500s, when an unknown printer took a galley of type and scrambled it to make a type specimen book. It has survived not only five centuries, but also the leap into electronic typesetting, remaining essentially unchanged. It was popularised in the 1960s with the release of Letraset sheets containing Lorem Ipsum passages, and more recently with desktop.</p>
    </div>
    <div class="feature-grid">
      <div class="feature">
        <svg viewBox="0 0 60 60"><circle cx="30" cy="30" r="17" fill="none" stroke="#1fb3b6" stroke-width="9" stroke-dasharray="7 4.5"/><circle cx="30" cy="30" r="7" fill="#1fb3b6"/></svg>
        <div><h3>Loads Of Settings</h3><p>Lorem Ipsum has been the industry's standard dummy text ever since the 1500s, when an unknown printer took a galley of type and scrambled it to make</p></div>
      </div>
      <div class="feature">
        <svg viewBox="0 0 60 60"><path d="M16 44a10 10 0 0 1 0-20 14 14 0 0 1 27-3 11 11 0 0 1 2 23z" fill="#1fb3b6"/></svg>
        <div><h3>Hosting In The Cloud</h3><p>Lorem Ipsum has been the industry's standard dummy text ever since the 1500s, when an unknown printer took a galley of type and scrambled it to make</p></div>
      </div>
      <div class="feature">
        <svg viewBox="0 0 60 60"><rect x="12" y="10" width="36" height="30" rx="4" fill="#1fb3b6"/><rect x="10" y="42" width="40" height="10" rx="2" fill="#1fb3b6"/><circle cx="43" cy="47" r="2" fill="#1b1b1b"/></svg>
        <div><h3>Unlimited Disk Space</h3><p>Lorem Ipsum has been the industry's standard dummy text ever since the 1500s, when an unknown printer took a galley of type and scrambled it to make</p></div>
      </div>
      <div class="feature">
        <svg viewBox="0 0 60 60"><circle cx="30" cy="30" r="22" fill="none" stroke="#1fb3b6" stroke-width="5"/><path d="M30 30l10-10" stroke="#1fb3b6" stroke-width="5" stroke-linecap="round"/><circle cx="30" cy="30" r="4" fill="#1fb3b6"/></svg>
        <div><h3>Amazing Performance Servers</h3><p>Lorem Ipsum has been the industry's standard dummy text ever since the 1500s, when an unknown printer took a galley of type and scrambled it to make</p></div>
      </div>
      <div class="feature">
        <svg viewBox="0 0 60 60"><rect x="8" y="18" width="44" height="30" rx="4" fill="#1fb3b6"/><path d="M22 18v-5h16v5" fill="none" stroke="#1fb3b6" stroke-width="4"/><rect x="8" y="30" width="44" height="3" fill="#1b1b1b"/></svg>
        <div><h3>Business Hosting Solutions</h3><p>Lorem Ipsum has been the industry's standard dummy text ever since the 1500s, when an unknown printer took a galley of type and scrambled it to make</p></div>
      </div>
      <div class="feature">
        <svg viewBox="0 0 60 60"><path d="M12 38v-8a18 18 0 0 1 36 0v8" fill="none" stroke="#1fb3b6" stroke-width="5"/><rect x="8" y="34" width="11" height="16" rx="3" fill="#1fb3b6"/><rect x="41" y="34" width="11" height="16" rx="3" fill="#1fb3b6"/></svg>
        <div><h3>24/7 Live Support</h3><p>Lorem Ipsum has been the industry's standard dummy text ever since the 1500s, when an unknown printer took a galley of type and scrambled it to make</p></div>
      </div>
    </div>
  </div>
</section>

<section class="blogs">
  <div class="wrap">
    <div class="sec-head">
      <h2 class="sec-title"><small>OUR LATEST</small><strong>BLOGS</strong></h2>
      <p>Lorem Ipsum has been the industry's standard dummy text ever since the 1500s, when an unknown printer took a galley of type and scrambled it to make a type specimen book. It has survived not only five centuries, but also the leap into electronic typesetting.</p>
    </div>
    <div class="blog-grid">
      <article class="post"><div class="thumb" role="img" aria-label="Blog photo of server hardware"></div><div><h3>Lorem simply dummy text of the industry</h3><time>November 01, 2015</time><p>Lorem Ipsum has been the industry's standard dummy text ever since the 1500s, when an unknown printer took.</p><a>Readmore</a></div></article>
      <article class="post"><div class="thumb" role="img" aria-label="Blog photo of a businessman"></div><div><h3>Lorem simply dummy text of the industry</h3><time>November 01, 2015</time><p>Lorem Ipsum has been the industry's standard dummy text ever since the 1500s, when an unknown printer took.</p><a>Readmore</a></div></article>
      <article class="post"><div class="thumb" role="img" aria-label="Blog photo of a man in a suit"></div><div><h3>Lorem simply dummy text of the industry</h3><time>November 01, 2015</time><p>Lorem Ipsum has been the industry's standard dummy text ever since the 1500s, when an unknown printer took.</p><a>Readmore</a></div></article>
      <article class="post"><div class="thumb" role="img" aria-label="Blog photo of a presenter"></div><div><h3>Lorem simply dummy text of the industry</h3><time>November 01, 2015</time><p>Lorem Ipsum has been the industry's standard dummy text ever since the 1500s, when an unknown printer took.</p><a>Readmore</a></div></article>
      <article class="post"><div class="thumb" role="img" aria-label="Blog photo of a handshake"></div><div><h3>Lorem simply dummy text of the industry</h3><time>November 01, 2015</time><p>Lorem Ipsum has been the industry's standard dummy text ever since the 1500s, when an unknown printer took.</p><a>Readmore</a></div></article>
      <article class="post"><div class="thumb" role="img" aria-label="Blog photo of a woman smiling"></div><div><h3>Lorem simply dummy text of the industry</h3><time>November 01, 2015</time><p>Lorem Ipsum has been the industry's standard dummy text ever since the 1500s, when an unknown printer took.</p><a>Readmore</a></div></article>
    </div>
  </div>
</section>

<section class="testimonials dark">
  <div class="wrap">
    <div class="sec-head">
      <h2 class="sec-title"><small>OUR CLIENT</small><strong>SAYS</strong></h2>
      <p>Lorem Ipsum has been the industry's standard dummy text ever since the 1500s, when an unknown printer took a galley of type and scrambled it to make a type specimen book. It has survived not only five centuries, but also the leap into electronic typesetting, remaining essentially unchanged. It was popularised in the 1960s with the release of Letraset sheets containing Lorem Ipsum passages, and more recently with desktop.</p>
    </div>
    <div class="quotes">
      <div class="quote left" style="left:0">
        <div><h4>Daniel Ashcombe</h4><div class="role">Marketing - <span>Brickwave</span></div><p>Lorem ipsum dolor sit amet, consectetur adipiscing elit et justo sit Suspendisse et justo.</p></div>
        <div class="avatar" role="img" aria-label="Client portrait"></div>
      </div>
      <div class="quote right" style="left:500px">
        <div class="avatar" role="img" aria-label="Client portrait"></div>
        <div><h4>Daniel Ashcombe</h4><div class="role">Marketing - <span>Brickwave</span></div><p>Lorem ipsum dolor sit amet, consectetur adipiscing elit et justo sit Suspendisse et justo.</p></div>
      </div>
    </div>
  </div>
</section>

<section class="stats" role="img" aria-label="Photo of a group of friends sitting arm in arm on a beach">
  <div class="stat-row">
    <div class="stat"><b>8564</b><span>Simply Dummy text</span><em>Chatterly</em></div>
    <div class="stat"><b>8564</b><span>Simply Dummy text</span><em>Quipster</em></div>
    <div class="stat"><b>8564</b><span>Simply Dummy text</span><em>workRing</em></div>
  </div>
</section>

<section class="clients">
  <div class="wrap">
    <div class="sec-head">
      <h2 class="sec-title"><small>SOME OF OUR</small><strong>CLIENTS</strong></h2>
      <p>Lorem Ipsum has been the industry's standard dummy text ever since the 1500s, when an unknown printer took a galley of type and scrambled it to make a type specimen book. It has survived not only five centuries, but also the leap into electronic typesetting.</p>
    </div>
    <div class="client-row">
      <span class="client"><i></i>KESTREL</span>
      <span class="client">NovaRise</span>
      <span class="client">FORMWELL</span>
      <span class="client">TIDE VERSE</span>
      <span class="client">SUNLOOP</span>
      <span class="client"><i></i>OPEN ORBIT</span>
    </div>
  </div>
</section>

<footer class="site-footer">
  <div class="wrap">
    <div class="footer-cols">
      <div class="footer-col"><h4>QUICK LINKS</h4>
        <ul><li>Home</li><li>About</li><li>Domains</li><li>Email</li><li>Hosting</li><li>Dedicated Server</li><li>Faq</li><li>Blog</li><li>Contact Us</li></ul></div>
      <div class="footer-col"><h4>SERVICES</h4>
        <ul><li>Domain Hosting</li><li>Sitedesigner</li><li>Web Hosting</li><li>Premium Web Hosting</li><li>Reseller Hosting</li><li>Virtual Private Servers</li><li>Hybrid Servers</li><li>Dedicated Servers</li><li>Email Hosting</li></ul></div>
      <div class="footer-col contact"><h4>CONTACT DETAILS</h4>
        <div><svg width="22" height="22" viewBox="0 0 22 22"><path d="M11 1a7 7 0 0 1 7 7c0 5-7 13-7 13S4 13 4 8a7 7 0 0 1 7-7z" fill="#1fb3b6"/><circle cx="11" cy="8" r="2.5" fill="#1b1b1b"/></svg><b style="color:#fff">Our Server Lantern</b><br>Dawn nursery Rich,<br>aukeulem tincidunt id lex<br>laoreet dolore magna<br>123456</div>
        <div class="phone"><svg width="22" height="22" viewBox="0 0 22 22"><path d="M5 2l4 4-2 3c1 3 3 5 6 6l3-2 4 4-3 3C9 20 2 13 2 5z" fill="#1fb3b6"/></svg>123-456-7890</div>
        <div><svg width="22" height="22" viewBox="0 0 22 22"><rect x="2" y="5" width="18" height="13" rx="2" fill="#1fb3b6"/><path d="M2 6l9 7 9-7" fill="none" stroke="#1b1b1b" stroke-width="1.5"/></svg>info@serverlantern.uk</div>
      </div>
    </div>
  </div>
  <div class="follow">
    <h4>FOLLOW US</h4>
    <div class="socials"><i></i><i></i><i></i><i></i><i></i><i></i></div>
    <h4>FOLLOW US</h4>
    <div class="newsletter">Email Address</div>
    <span class="submit">SUBMIT</span>
  </div>
</footer>

<div class="bottom-bar">
  <div class="wrap">
    <span>Copyright © 2015 Our Server Lantern, Inc. All rights reserved.</span>
    <nav><span>Support</span><span>Privacy</span><span>Terms</span></nav>
  </div>
</div>

</body>
</html>
```